Business Cards used to invite people to our church

We are a church and have need of a business card sized advertisement that allows our members to hand them out in order to invite people to the church. I need the front of the card to say "You're Invited" or "Come Check us out". with the service times on the back of the card later.
I have attached one of the OLD cards we have used in the past, but we want a complete makeover, into a more modern style that does not require the image.
I am also replacing the old logo with a newer "flat" logo which is attached.
Please use marketing colors. (blue or red or something that catches attention)
Create a card that DOES NOT have the picture of the two people on the front
The information on the sample card back is correct to go onto new card
Target Market(s)
anyone
Industry/Entity Type
Business
Contact Information for Business Card
sertice times and address information which you can get from the sample card I uploaded. It should have "You're Invited" or "Come Check us out" on the front of the card with out logo.

```html
<!DOCTYPE html>
<html lang="en">
<head>
<meta charset="utf-8">
<title>Grace Harbor Ministries – Invitation Card</title>
<link rel="stylesheet" href="https://fonts.googleapis.com/css2?family=Open+Sans:ital,wght@0,600;1,700&family=Great+Vibes&display=swap">
<style>
  :root {
    --backdrop: #2e2f33;
    --card-red: #ff0000;
    --ink-white: #ffffff;
    --card-shadow: rgba(0, 0, 0, 0.45);
  }
  * { margin: 0; padding: 0; box-sizing: border-box; }
  html, body {
    width: 1200px;
    height: 864px;
    overflow: hidden;
    background: var(--backdrop);
  }
  .canvas {
    position: relative;
    width: 1200px;
    height: 864px;
  }
  .card {
    position: absolute;
    left: 300px;
    width: 600px;
    height: 340px;
    background: var(--card-red);
    color: var(--ink-white);
    box-shadow: 0 10px 24px var(--card-shadow);
  }
  .card--back { top: 50px; }
  .card--front { top: 470px; }

  /* Back: contact row */
  .contact-row {
    position: absolute;
    top: 22px;
    left: 28px;
    right: 28px;
    display: flex;
    justify-content: space-between;
    font-family: "Open Sans", sans-serif;
    font-weight: 700;
    font-style: italic;
    font-size: 12.5px;
  }
  .contact-item { display: flex; align-items: center; gap: 8px; }
  .contact-item svg { width: 11px; height: 11px; fill: var(--ink-white); }

  /* Back: ministry name */
  .ministry-name {
    position: absolute;
    top: 96px;
    left: 0;
    right: 0;
    text-align: center;
    font-family: "Open Sans", sans-serif;
    font-weight: 600;
    font-size: 26px;
    letter-spacing: 0.04em;
  }

  /* Back: service times */
  .service-times {
    position: absolute;
    top: 178px;
    left: 150px;
    width: 300px;
    list-style: none;
    font-family: "Open Sans", sans-serif;
    font-weight: 700;
    font-style: italic;
    font-size: 13.5px;
  }
  .service-times li {
    display: flex;
    align-items: baseline;
    margin-bottom: 9px;
  }
  .service-times .leader {
    flex: 1;
    border-bottom: 2px dotted var(--ink-white);
    margin: 0 4px;
    transform: translateY(-3px);
  }

  /* Front: invitation */
  .invite {
    position: absolute;
    font-family: "Great Vibes", cursive;
    font-size: 70px;
    line-height: 1;
    white-space: nowrap;
  }
  .invite--first { top: 100px; left: 80px; }
  .invite--second { top: 190px; left: 210px; }
</style>
</head>
<body>
<main class="canvas">
  <section class="card card--back" aria-label="Card back with service times">
    <div class="contact-row">
      <span class="contact-item">
        <svg viewBox="0 0 12 12" aria-hidden="true"><path d="M6 0a4 4 0 0 0-4 4c0 3 4 8 4 8s4-5 4-8a4 4 0 0 0-4-4zm0 5.6A1.6 1.6 0 1 1 6 2.4a1.6 1.6 0 0 1 0 3.2z"/></svg>
        2480. Alder Lane - Brookvale, Tx 75990
      </span>
      <span class="contact-item">
        <svg viewBox="0 0 12 12" aria-hidden="true"><path d="M2.5 0.5l2 2.2-1 1.3c.8 1.7 2 2.9 3.6 3.7l1.3-1 2.1 2-1.2 2.3C5 10.5 1.4 7 .8 2z"/></svg>
        1-800-555-0142
      </span>
    </div>

    <h1 class="ministry-name">GRACE HARBOR MINISTRIES</h1>

    <ul class="service-times">
      <li><span>Sunday</span><span class="leader"></span><span>9:00 Am</span></li>
      <li><span>Sunday</span><span class="leader"></span><span>11.00 Am</span></li>
      <li><span>Web. Bible Class</span><span class="leader"></span><span>7:00 Pm</span></li>
    </ul>
  </section>

  <section class="card card--front" aria-label="Card front invitation">
    <p class="invite invite--first">You 're</p>
    <p class="invite invite--second">Invited</p>
  </section>
</main>
</body>
</html>
```